Australian Web Design company needs a business card design

We need a business card design for a Sydney based Web Design/Development company called "Blue Pine Web Design". We design, build and deploy websites for small to medium sized businesses. The final design should be clean and communicate that we are a professional and supportive company.
I'd like the Icon to be abstract. Something that embodies the power of the internet, needs to be clean/professional and show that we are human and that we support our customers. Hope that helps.
Target Market(s)
All small to medium businesses
Industry/Entity Type
Business
Contact Information for Business Card
Gordon Whitcombe
Blue Pine Web Design
17 Calloway Brook Road
East Gosford
NSW 2250
0438 572 614
gordon@bluepinewebdesign.com.au
www.bluepinewebdesign.com.au

```html
<!DOCTYPE html>
<html lang="en">
<head>
<meta charset="utf-8">
<title>Blue Pine Web Design – Business Card</title>
<link href="https://fonts.googleapis.com/css2?family=Michroma&family=Ubuntu:ital,wght@0,400;0,500;1,500&display=swap" rel="stylesheet">
<style>
  :root {
    --maroon: #7a1c34;
    --maroon-deep: #6b1530;
    --ink: #4a4a4c;
    --paper: #ffffff;
    --stage: #e9e7e4;
    --mute: #e4e4e4;
  }
  * { box-sizing: border-box; margin: 0; padding: 0; }
  html, body { width: 1200px; height: 848px; overflow: hidden; }
  body {
    background: var(--stage);
    font-family: "Ubuntu", sans-serif;
    display: flex;
    align-items: center;
    justify-content: center;
    gap: 60px;
  }
  .card {
    width: 520px;
    height: 316px;
    border-radius: 4px;
    box-shadow: 0 6px 18px rgba(0,0,0,.15);
    position: relative;
    overflow: hidden;
  }
  /* Front */
  .card--front { background: var(--paper); padding: 34px 38px; }
  .card__accent {
    position: absolute;
    right: -40px;
    bottom: -70px;
    width: 260px;
    height: 260px;
    border-radius: 50%;
    background: var(--mute);
  }
  .card--front > *:not(.card__accent) { position: relative; }
  .brand { display: flex; align-items: center; gap: 10px; }
  .brand__dot { width: 26px; height: 26px; border-radius: 50%; background: var(--maroon); flex: none; }
  .brand__name { font-size: 19px; font-weight: 500; color: var(--maroon); letter-spacing: .5px; }
  .person { margin-top: 30px; }
  .person__name {
    font-family: "Michroma", sans-serif;
    font-weight: 400;
    font-size: 19px;
    letter-spacing: 4px;
    color: var(--ink);
    text-transform: uppercase;
  }
  .person__title {
    margin-top: 6px;
    font-size: 14px;
    font-weight: 500;
    font-style: italic;
    color: var(--maroon);
  }
  .contact { list-style: none; margin-top: 20px; }
  .contact__item {
    display: flex;
    align-items: flex-start;
    gap: 8px;
    font-size: 13px;
    line-height: 18px;
    color: var(--ink);
    margin-bottom: 3px;
  }
  .contact__icon { width: 13px; height: 13px; flex: none; margin-top: 2px; }
  /* Back */
  .card--back {
    background: var(--maroon-deep);
    display: flex;
    flex-direction: column;
    align-items: center;
    justify-content: center;
    gap: 26px;
  }
  .card--back .brand__dot { width: 40px; height: 40px; background: var(--paper); }
  .card--back .brand__name { font-size: 28px; color: var(--paper); }
  .site { font-size: 16px; font-weight: 500; font-style: italic; color: var(--paper); letter-spacing: .3px; }
</style>
</head>
<body>
  <article class="card card--front">
    <span class="card__accent"></span>
    <div class="brand">
      <span class="brand__dot"></span>
      <span class="brand__name">Blue Pine Web Design</span>
    </div>
    <div class="person">
      <h1 class="person__name">Gordon Whitcombe</h1>
      <p class="person__title">B.Eng (Hons) First Class</p>
    </div>
    <ul class="contact">
      <li class="contact__item">
        <svg class="contact__icon" viewBox="0 0 14 14"><circle cx="7" cy="7" r="7" fill="#7a1c34"/><path d="M7 3.2a2.4 2.4 0 0 0-2.4 2.4C4.6 7.4 7 10.8 7 10.8s2.4-3.4 2.4-5.2A2.4 2.4 0 0 0 7 3.2z" fill="#fff"/><circle cx="7" cy="5.6" r=".9" fill="#7a1c34"/></svg>
        <span>17 Calloway Brook Road,<br>Wattle Ridge NSW 2261</span>
      </li>
      <li class="contact__item">
        <svg class="contact__icon" viewBox="0 0 14 14"><circle cx="7" cy="7" r="7" fill="#7a1c34"/><path d="M4.6 3.6l1.4-.3.7 1.8-.9.7a5 5 0 0 0 2.4 2.4l.7-.9 1.8.7-.3 1.4C8 9.6 4.4 6 4.6 3.6z" fill="#fff"/></svg>
        <span>0438 572 614</span>
      </li>
      <li class="contact__item">
        <svg class="contact__icon" viewBox="0 0 14 14"><circle cx="7" cy="7" r="7" fill="#7a1c34"/><rect x="3.6" y="4.6" width="6.8" height="4.8" rx=".5" fill="#fff"/><path d="M3.8 4.9L7 7.3l3.2-2.4" fill="none" stroke="#7a1c34" stroke-width=".7"/></svg>
        <span>gordon@bluepinewebdesign.com.au</span>
      </li>
    </ul>
  </article>

  <article class="card card--back">
    <div class="brand">
      <span class="brand__dot"></span>
      <span class="brand__name">Blue Pine Web Design</span>
    </div>
    <p class="site">bluepinewebdesign.com.au</p>
  </article>
</body>
</html>
```